Company's Core Values to be on our Office Walls

We are a biotechnology consulting company in Massachusetts with about 40 employees. Please check out velmora.com for our look and more information on our business.

We have 4 core values in the company which we would like to display in our office. (Could be on our walls, could be placed in our website, could be placed anywhere. - We would like a multi-use for this graphic but PRIMARILY on our walls.)
No measurements involved yet, hence we'd like the source file to enable us to stretch the graphics. What's important is to see the designs in this contest.

Design: Looking for a wall display - decal, glass board, vinyl (we're open)
- of our Core Values to have in our reception. We want a Double-Helix
incorporated as the core values are "in our DNA" like the one attached
(would like to see some designs with the exact photo and some used as
inspiration for a unique creative design). Open to various sizes, we have a
few different walls we could place them on.

We are looking for a creative Core Value display to have in our new office. We want a sleek, out of the box design!

Velmora's 4 Core Values are:
> Put Others First
> Have the Courage to Take Action
> Take Personal Responsibility
> Have fun!
***We welcome any infographics per core value. We are open to your creativity!

**WE WANT THE ACTUAL CORE VALUES ON DISPLAY**
We already have a brand (attached).
Need our actual values on display in office.
We want the actual values on the wall, our logo can be incorporated but not
necessarily.

Overview of company: Young consulting firm for biotech and pharmaceuticals
in the Greater Boston area. We are service based, our employees are
engineers and specialists that work on our clients site. Company was
established in 2010, we moved into our New England office 3 months ago!

Colors: Our main color is blue but we also use orange, green, purple, and
teal. See velmora.com for our colors.

Target Market(s)

New Hires and Clients - We want to impress them!
Employees and clients - we want employees inspired by the core
values and clients to be impressed by them/separate us from the competition.

Industry/Entity Type

Biotechnology

Font styles to use
Sans Serif

Colors

Designer to choose colors to be used in the design.

Requirements
Must have
• Creativity!
• Some sort of tie to science/biotech
• Color - Blue is our company color but would like others as well. See website for brand colors.

```html
<!DOCTYPE html>
<html lang="en">
<head>
<meta charset="utf-8">
<title>Velmora Core Values</title>
<link href="https://fonts.googleapis.com/css2?family=Exo+2:wght@800&display=swap" rel="stylesheet">
<style>
  :root {
    --navy: #0f3b5f;
    --blue: #1766a3;
    --paper: #ffffff;
  }
  html, body {
    margin: 0;
    padding: 0;
    width: 1199px;
    height: 1200px;
    overflow: hidden;
    background: var(--paper);
  }
  .values-display {
    width: 1199px;
    height: 1200px;
    display: flex;
    align-items: center;
    justify-content: center;
    gap: 26px;
  }
  .helix-motif {
    width: 160px;
    height: 320px;
    flex: none;
    background: linear-gradient(90deg, var(--blue) 0%, var(--navy) 100%);
    opacity: 0.85;
  }
  .value-list {
    list-style: none;
    margin: 18px 0 0;
    padding: 0;
    font-family: "Exo 2", sans-serif;
    font-weight: 800;
    font-size: 51px;
    line-height: 69px;
    text-transform: uppercase;
    letter-spacing: -0.5px;
    white-space: nowrap;
  }
  .value-list .navy { color: var(--navy); }
  .value-list .blue { color: var(--blue); }
</style>
</head>
<body>
  <main class="values-display">
    <div class="helix-motif" role="img" aria-label="Dotted double-helix DNA motif in navy and blue"></div>
    <ul class="value-list">
      <li class="navy">Put others first</li>
      <li class="blue">Have the courage to take action</li>
      <li class="navy">Take personal responsibility</li>
      <li class="blue">Have fun!</li>
    </ul>
  </main>
</body>
</html>
```